Luxurious Rustic Cottage Accommodation brochure design

I would like a trifold brochure design to continue the theme I already have established on my website www.atbellowvale.com.au The basic theme uses the logo from the website, it is called "At Dunforths" B & B Private Cottages and has black background with use of gold for borders and highlights. The accommodation is in the hinterland region of the Sunshine Coast, Queensland, Australia. I have 4 separate private cottages which I would like to include information & pictures about each as per details on the website mentioned. Features to highlight include ocean views, log fires, spa baths, romance, nature. Accommodation is suitable for couples, family, small group or wedding party, special occasion getways. Package inclusions to be highlighted are breakfast hamper, complimentary chocolates & champagne, pamper products, optional inclusions are cheese platter, relaxation massage. I would like location to be included by way of a map, contact details (website, email & mobile phone) to also be included.
There are pictures on the website which I can provide high resolution for brochure printing as required. Some more images have been uploaded for optional use.

```html
<!DOCTYPE html>
<html lang="en">
<head>
<meta charset="utf-8">
<title>At Dunforths – Brochure Inside Spread</title>
<link href="https://fonts.googleapis.com/css2?family=Cardo:ital,wght@0,400;1,400&family=Lato:ital,wght@0,400;0,700;1,700&display=swap" rel="stylesheet">
<style>
  :root {
    --bg-dark: #262626;
    --bg-mid: #333333;
    --paper: #ffffff;
    --ink: #1c1c1c;
    --text-light: #f2f2f2;
    --label-veil: rgba(255,255,255,0.82);
    --photo-warm: #b98a5a;
    --photo-green: #5d7048;
    --photo-cream: #e8e2d6;
    --photo-red: #b8322a;
  }
  * { box-sizing: border-box; margin: 0; padding: 0; }
  html, body { width: 1200px; height: 933px; overflow: hidden; }
  body {
    position: relative;
    background: radial-gradient(ellipse at 50% 40%, var(--bg-mid), var(--bg-dark) 75%);
    font-family: "Lato", sans-serif;
    color: var(--text-light);
  }
  .panel-title {
    position: absolute; top: 23px; height: 41px;
    background: var(--paper); color: var(--ink);
    font-family: "Cardo", serif; font-size: 27px;
    display: flex; align-items: center; justify-content: center;
  }
  .col-about { left: 16px; width: 385px; }
  .col-cabins { left: 408px; width: 391px; }
  .col-rates { left: 806px; width: 379px; }

  .photo { position: absolute; }
  .family-photo {
    top: 70px; left: 16px; width: 384px; height: 288px;
    border: 3px solid var(--paper);
    background: linear-gradient(120deg, var(--photo-green) 0%, #8c8a6a 35%, var(--photo-red) 70%, #6f2a22 100%);
  }
  .about-text {
    position: absolute; top: 372px; left: 16px; width: 385px;
    text-align: center; font-size: 20.5px; line-height: 29px;
  }
  .signature {
    position: absolute; top: 669px; left: 130px; width: 270px;
    text-align: right; font-weight: 700; font-size: 20.5px;
  }
  .contact {
    position: absolute; top: 742px; left: 16px; width: 385px;
    text-align: center; font-size: 19px; line-height: 24px;
  }
  .contact h3 { font-size: 21px; font-weight: 700; }

  .cabin {
    position: absolute; left: 408px; width: 391px;
  }
  .cabin-label {
    position: absolute; right: 0; top: 0; width: 165px;
    background: var(--label-veil); color: var(--ink);
    font-family: "Cardo", serif; font-style: italic; font-size: 22px;
    text-align: right; padding: 3px 10px 2px;
  }
  .cabin-features {
    position: absolute; right: 0; width: 165px;
    background: rgba(255,255,255,0.55); color: var(--ink);
    font-family: "Cardo", serif; font-size: 11.5px; line-height: 14px;
    text-align: center; padding: 5px 4px;
  }
  .cabin-1 { top: 70px; height: 208px; background: linear-gradient(160deg, var(--photo-cream), #f5f3ef 50%, #c7a067 80%, #f0ece4); }
  .cabin-2 { top: 278px; height: 218px; background: linear-gradient(150deg, #8a9aa8, var(--photo-warm) 35%, var(--photo-green) 65%, #3d4a2e); }
  .cabin-3 { top: 496px; height: 211px; background: linear-gradient(170deg, #5c5248, #8d7f70 40%, var(--photo-cream) 70%, #f3f0ea); }
  .cabin-4 { top: 707px; height: 198px; background: linear-gradient(165deg, #e8e6e0, var(--photo-green) 35%, #7a5a3a 65%, #4b3320); }

  .rate-box {
    position: absolute; left: 806px; width: 379px;
    background: var(--paper); color: var(--ink);
    font-size: 20px; line-height: 27px; text-align: center;
  }
  .rate-couples { top: 80px; height: 67px; padding-top: 6px; }
  .rate-lodge { top: 309px; height: 39px; padding-top: 6px; }
  .rate-row {
    position: absolute; left: 846px; width: 308px;
    display: flex; justify-content: space-between;
    font-family: "Cardo", serif; font-size: 20px;
  }
  .rate-note { display: block; font-size: 16px; line-height: 17px; }
  .inclusions {
    position: absolute; left: 806px; width: 379px; text-align: center;
    font-size: 20px; line-height: 29px;
  }
  .inclusions h4 { font-style: italic; font-weight: 700; font-size: 21px; }
</style>
</head>
<body>
  <h2 class="panel-title col-about">About Us</h2>
  <h2 class="panel-title col-cabins">Cabins</h2>
  <h2 class="panel-title col-rates">Rates &amp; Packages</h2>

  <div class="photo family-photo" role="img" aria-label="Family of five with their dog sitting beside a red vintage hot rod"></div>
  <p class="about-text">We are classic “treechangers” and together with our 3 daughters we moved to Queensland from Northern NSW in 2005 to enjoy the beautiful hinterland lifestyle and establish our B &amp; B. We love to have a chat, share our local knowledge and ensure you have everything to make your stay enjoyable, otherwise we pretty much leave you to enjoy your own company.</p>
  <p class="signature">- Grant &amp; Leanne Whitford</p>
  <div class="contact">
    <h3>Contact Us</h3>
    <p>Ph: 0412 555 308</p>
    <p>Email: leanne@atdunforths.com.au</p>
  </div>

  <section class="cabin cabin-1" role="img" aria-label="King size bed with breakfast tray and flowers">
    <div class="cabin-label">Drovers Rest</div>
    <div class="cabin-features" style="top:40px">- Luxurious king size bed<br>- Indoor/outdoor spa bath</div>
  </section>
  <section class="cabin cabin-2" role="img" aria-label="Timber cottage with red roof among garden plants">
    <div class="cabin-label">Kooringa</div>
    <div class="cabin-features" style="top:34px">- Hinterland &amp; ocean view<br>- Surrounded by<br>fragrant timber,<br>camphor furniture</div>
  </section>
  <section class="cabin cabin-3" role="img" aria-label="Bedroom with log fire and bistro table">
    <div class="cabin-label">Wattlebrae</div>
    <div class="cabin-features" style="top:34px">- Hinterland &amp; coastal views<br>- Spa bath &amp; log fire<br>- King size bed</div>
  </section>
  <section class="cabin cabin-4" role="img" aria-label="Lodge deck with outdoor furniture and spa among trees">
    <div class="cabin-label">Lodge</div>
    <div class="cabin-features" style="top:34px">- Ocean &amp; hinterland views<br>- 4 bedrooms</div>
  </section>

  <div class="rate-box rate-couples">Couples Cabin,<br>Wattlebrae Guest wing</div>
  <div class="rate-row" style="top:168px"><span>7 night Stay</span><span>$1595</span></div>
  <div class="rate-row" style="top:206px"><span>Weekend Stay</span><span>$295/Night</span></div>
  <div class="rate-row" style="top:248px"><span>Midweek Stay</span><span>$195 - $245/Night</span></div>

  <div class="rate-box rate-lodge">4 Bedroom Lodge</div>
  <div class="rate-row" style="top:365px"><span>Weekend(2 nights)<span class="rate-note">Up to 8 guests</span></span><span>$1200</span></div>
  <div class="rate-row" style="top:420px"><span>Midweek<span class="rate-note">Up to 8 guests</span></span><span>$275 - $350/Night</span></div>

  <div class="inclusions" style="top:566px">
    <h4>* Package Inclusions</h4>
    <p>Breakfast hamper, ,Champagne,<br>Pamper products &amp;<br>complimentary chocolates.</p>
  </div>
  <div class="inclusions" style="top:703px">
    <h4>* Optional Inclusions</h4>
    <p>Cheese platter<br>&amp;<br>Relaxation massage.</p>
  </div>
</body>
</html>
```